Design a New Tennis and Athletic Club- Business cards desired with a wow factor.

Help us find a exciting and useful design for our business.
1. Design should be two-sided made of materials that will last.
2. Eye-popping graphics
3. Space for changeable quotes on the back of our card with our "wolf" program logo.
4. Recolor wolf to match club colors

Target Market(s)

Players parents coaches clients

Industry/Entity Type

Business

Contact Information for Business Card

Birchwood Paddle + Wellness
Derek Hollins
Director of Tennis Operations
2817 Meadowcrest Ave NE
Grand Rapids Michigan 49318
Office (616) 555-0142
Cell (269) 555-0186
Email dhollins482@mailbox-example.com
Website http://www.bwpaddle-example.com
Facebook https://www.facebook.com/BWPaddleExample

Font styles to use
Serif

Colors
0555a3
f37122
ffffff

Requirements
Must have
• 1.interesting contemporary design,
• 2. 2 sided
• 3. ability to swap out staff information for other trainers and professionals
Nice to have
• 1.Space for changeable quotes on the back of the card
• 2. change wolf logo body to match club color blue
• 3. some white space on card for notes to be written.
Should not have
• boring same old consruction

```html
<!DOCTYPE html>
<html lang="en">
<head>
<meta charset="utf-8">
<title>Birchwood Paddle + Wellness – Business Card</title>
<link href="https://fonts.googleapis.com/css2?family=Roboto:wght@400;500;700&family=Roboto+Condensed:wght@700&display=swap" rel="stylesheet">
<style>
  :root {
    --stage: #d9d6d1;
    --navy: #161a3a;
    --navy-ink: #1c2046;
    --orange: #e0552f;
    --white: #ffffff;
    --paper: #f2f2f2;
    --rule: #6d7090;
    --grey-text: #555a66;
    --badge-blue: #2160b0;
  }
  * { box-sizing: border-box; margin: 0; padding: 0; }
  html, body { width: 1200px; height: 960px; overflow: hidden; }
  body {
    position: relative;
    background: var(--stage);
    font-family: "Roboto", Arial, sans-serif;
  }
  .card {
    position: absolute;
    width: 598px;
    height: 342px;
    border-radius: 22px;
    box-shadow: 0 3px 6px rgba(0,0,0,0.25);
  }
  .card-front { left: 315px; top: 113px; background: var(--navy); color: var(--white); }
  .card-back { left: 311px; top: 472px; width: 600px; background: var(--paper); }

  .staff-name {
    position: absolute; left: 33px; top: 34px;
    font-family: "Roboto Condensed", "Roboto", sans-serif;
    font-weight: 700; font-size: 21px; color: var(--orange); letter-spacing: 0.2px;
  }
  .staff-title { position: absolute; left: 33px; top: 58px; font-size: 15px; font-weight: 500; }
  .rule {
    position: absolute; left: 33px; width: 253px; height: 0;
    border-top: 1px dashed var(--rule);
  }
  .rule-top { top: 100px; }
  .rule-bottom { top: 185px; }
  .address { position: absolute; left: 33px; top: 127px; font-size: 14px; line-height: 19px; }
  .contacts { position: absolute; left: 35px; top: 214px; list-style: none; font-size: 14px; }
  .contacts li { display: flex; align-items: center; height: 19.3px; }
  .contacts svg { width: 12px; height: 12px; margin-right: 10px; flex: none; }
  .icon-square { width: 11px; height: 11px; background: var(--orange); border-radius: 2px; margin-right: 11px; flex: none; }

  .front-wordmark {
    position: absolute; right: 18px; top: 130px;
    font-weight: 700; font-size: 58px; color: var(--white); letter-spacing: -1px;
  }

  .partner-badge {
    position: absolute; left: 486px; top: 27px; width: 82px; height: 58px;
    background: var(--badge-blue);
  }
  .back-wordmark {
    position: absolute; left: 0; right: 0; top: 118px; text-align: center;
    font-weight: 700; font-size: 52px; color: var(--navy-ink); letter-spacing: -1px;
  }
  .back-tagline {
    position: absolute; left: 0; right: 0; top: 229px; text-align: center;
    font-weight: 500; font-size: 19px; color: var(--navy-ink); letter-spacing: 0.5px;
  }
  .back-web {
    position: absolute; left: 0; right: 0; top: 297px; text-align: center;
    font-size: 14px; color: var(--grey-text); letter-spacing: 5px;
  }
</style>
</head>
<body>

<section class="card card-front" aria-label="Card front">
  <h1 class="staff-name">DEREK HOLLINS</h1>
  <p class="staff-title">Director of Tennis Operations</p>
  <div class="rule rule-top"></div>
  <p class="address">2817 Meadowcrest Ave NE<br>Grand Rapids Michigan 49318</p>
  <div class="rule rule-bottom"></div>
  <ul class="contacts">
    <li>
      <svg viewBox="0 0 12 12"><path fill="#e0552f" d="M2.4 0.6l2 2.2-1 1.4c.7 1.5 1.9 2.7 3.4 3.4l1.4-1 2.2 2-1 2.6C4.8 11.2.8 7.2.2 1.6z"/></svg>
      616 555-0142
    </li>
    <li>
      <svg viewBox="0 0 12 12"><rect x="2.5" y="0" width="7" height="12" rx="1.2" fill="#e0552f"/><rect x="3.7" y="1.5" width="4.6" height="7.5" fill="#161a3a"/></svg>
      269 555-0186
    </li>
    <li>
      <svg viewBox="0 0 12 12"><circle cx="6" cy="6" r="5.5" fill="#e0552f"/><path d="M0.8 6h10.4M6 .5c-2.5 3-2.5 8 0 11M6 .5c2.5 3 2.5 8 0 11" stroke="#161a3a" stroke-width="1" fill="none"/></svg>
      www.bwpaddle-example.com
    </li>
    <li><span class="icon-square"></span>/BWPaddleExample</li>
    <li><span class="icon-square"></span>bwpaddle-example.com</li>
  </ul>
  <div class="front-wordmark">Birchwood</div>
</section>

<section class="card card-back" aria-label="Card back">
  <div class="partner-badge" role="img" aria-label="Partner program badge"></div>
  <div class="back-wordmark">Birchwood</div>
  <p class="back-tagline">PADDLE + WELLNESS</p>
  <p class="back-web">www.bwpaddle-example.com</p>
</section>

</body>
</html>
```